Visitenkarten
Zielgruppe
Hallo!
Für mein Unternehmen habe ich bereits einmal ein Logo mit Feldmotte erstellen lassen (leider weiß ich den Designer nicht mehr).
Unter meinem Unternehmen Vollmerhaus Coaching laufen zwei Unternehmensbereiche, für die ich jetzt Visitenkarten benötige. Daher ist der Stil der beiden Teilbereiche ähnlich. Die Logos existieren schon. Nun benötige ich für beide Bereiche Visitenkarten. Für beide Bereiche benötige ich im Anschluss im 1:1 Auftrage noch Dateien, damit die ich Logos auch gut auf Webseiten und Social Medien nutzen kann.
Vollmerhaus HR Services <: bietet HR Dienstleistungen rund um das Personalwesen an: HR-Trainings, HR Outsourcing und Projekt- und Interimsmanagement
Sattelklar Balance | Vollmerhaus Coaching: bietet Mental- und Hypnosecoachings an, Trainings zur mentalen Fitness, Stress- und Blockadenlösung im Reitsport und optimale Turniervorbereitung
Aufgabenstellung
Bitte den bestehenden Brandguide und die Materialien nutzen. Eigene Ideen sind willkommen, sollen aber in der Logik bleiben.
Daten Visitenkarte Vollmerhaus HR Services:
Annelie Vollmerhaus
Dipl. Sozialwirt, Business Coach, Mentaltrainer
Telefon +49 (0)1593 26 48 357
Mobil +49 (0)171 58 93 704
Mail: annelie@vollmerhaus-beratung.example
Vollmerhaus HR Services | Vollmerhaus Coaching
Am Lindenhang 9b
31847 Wiesental
Daten Visitenkarte Vollmerhaus Sattelklar Balance:
Dipl. Sozialwirt, Hypnosecoach, Mentaltrainer
Sattelklar Balance | Vollmerhaus Coaching

```html
<!DOCTYPE html>
<html lang="de">
<head>
<meta charset="utf-8">
<title>Visitenkarten – Sattelklar Balance</title>
<link rel="stylesheet" href="https://fonts.googleapis.com/css2?family=Montserrat:wght@300;400;600;700&display=swap">
<style>
  :root {
    --backdrop: #e6e6e8;
    --paper: #f4f4f3;
    --violet: #5d4a9c;
    --violet-deep: #3e2f7a;
    --violet-light: #8a7cc0;
    --lavender: #d9d5ea;
    --navy: #1c1446;
    --ink: #5a4c96;
    --ink-soft: #7a7399;
  }
  * { margin: 0; padding: 0; box-sizing: border-box; }
  html, body { width: 1200px; height: 854px; overflow: hidden; }
  body {
    background: var(--backdrop);
    font-family: "Montserrat", Arial, sans-serif;
    position: relative;
  }
  .card {
    position: absolute;
    width: 480px;
    height: 290px;
    border-radius: 3px;
    overflow: hidden;
    box-shadow: 0 6px 18px rgba(0,0,0,.12);
  }
  .card--front-violet {
    left: 90px; top: 110px;
    background: linear-gradient(160deg, var(--violet-light) 0%, var(--violet) 45%, var(--violet-deep) 100%);
  }
  .card--front-white {
    left: 630px; top: 110px;
    background: var(--paper);
  }
  .card--back {
    left: 360px; top: 470px;
    background: var(--paper);
  }
  .brand {
    position: absolute;
    inset: 0;
    display: flex;
    align-items: center;
    justify-content: center;
    gap: 14px;
  }
  .brand__dot {
    width: 16px; height: 16px;
    border-radius: 50%;
  }
  .brand__name {
    font-weight: 600;
    font-size: 22px;
    letter-spacing: .08em;
    text-transform: uppercase;
  }
  .card--front-violet .brand__dot { background: #ffffff; }
  .card--front-violet .brand__name { color: #ffffff; }
  .card--front-white .brand__dot { background: var(--violet); }
  .card--front-white .brand__name { color: var(--violet); }

  .back__shapes { position: absolute; inset: 0; }
  .contact {
    position: absolute;
    left: 30px; top: 46px;
    color: var(--ink);
  }
  .contact__name {
    font-weight: 700;
    font-size: 17px;
    letter-spacing: .03em;
    text-transform: uppercase;
  }
  .contact__role {
    font-weight: 300;
    font-size: 9.5px;
    color: var(--ink-soft);
    margin-top: 3px;
  }
  .contact__lines {
    margin-top: 26px;
    font-size: 8.5px;
    border-collapse: collapse;
  }
  .contact__lines th {
    text-align: left;
    font-weight: 600;
    padding: 1.5px 8px 1.5px 0;
  }
  .contact__lines td { font-weight: 400; padding: 1.5px 0; }
  .address {
    margin-top: 22px;
    font-weight: 300;
    font-size: 11px;
    line-height: 1.45;
    color: var(--ink-soft);
  }
</style>
</head>
<body>

  <section class="card card--front-violet" aria-label="Vorderseite violett">
    <div class="brand">
      <span class="brand__dot"></span>
      <span class="brand__name">Sattelklar Balance</span>
    </div>
  </section>

  <section class="card card--front-white" aria-label="Vorderseite weiß">
    <div class="brand">
      <span class="brand__dot"></span>
      <span class="brand__name">Sattelklar Balance</span>
    </div>
  </section>

  <section class="card card--back" aria-label="Rückseite mit Kontaktdaten">
    <svg class="back__shapes" width="480" height="290" viewBox="0 0 480 290" aria-hidden="true">
      <polygon points="260,290 360,0 480,0 480,290" fill="var(--lavender)"/>
      <polygon points="330,0 480,0 480,30 410,30" fill="var(--navy)"/>
      <polygon points="300,60 480,60 480,110 360,110" fill="var(--violet-deep)"/>
      <polygon points="360,110 480,110 480,290 310,290" fill="var(--violet)"/>
      <polygon points="0,262 320,262 310,290 0,290" fill="var(--violet)"/>
    </svg>
    <div class="contact">
      <h1 class="contact__name">Annelie Vollmerhaus</h1>
      <p class="contact__role">Dipl. Sozialwirt, Business Coach, Mentaltrainer</p>
      <table class="contact__lines">
        <tr><th>Telefon</th><td>: +49 (0)1593 26 48 357</td></tr>
        <tr><th>Mobil</th><td>: +49 (0)171 58 93 704</td></tr>
        <tr><th>Mail</th><td>: annelie@vollmerhaus-beratung.example</td></tr>
      </table>
      <p class="address">
        Sattelklar Balance | Vollmerhaus Coaching<br>
        Am Lindenhang 9b<br>
        31847 Wiesental
      </p>
    </div>
  </section>

</body>
</html>
```